Supplement Manufacture needs a label designed

We need a label design done for a patented supplement for pain management. We would like to see designs that include a shade of blue as the main color. We would like the label to be noticeable amongst the crowded field and position our product to be selected based on the beauty of the label. We have attached a label that we created but it is not what we need but it shows the color blue we prefer. Please visit our website for more information. www.kavroplex.net.

Target Market(s)

Health conscious individuals, Individuals who are looking for 100% all natural supplements.

Industry/Entity Type

Health And Wellness

Font styles to use
Serif

Colors
2f74b4
9bcb3c
f8a142
fbed22

Requirements
Must have
• Must have professional look and fit on 150cc HDPE packer bottle. Must meet US QBR label requirements.

```html
<!DOCTYPE html>
<html lang="en">
<head>
<meta charset="utf-8">
<title>KVX Kinetic Vitality Complex – Label</title>
<link rel="stylesheet" href="https://fonts.googleapis.com/css2?family=Tinos&family=Open+Sans:ital,wght@0,400;0,700;1,700&display=swap">
<style>
  :root {
    --blue: #2f74b4;
    --blue-light: #3a8fd0;
    --blue-dark: #1f5d99;
    --ink: #1a1a1a;
    --paper: #ffffff;
    --backdrop: #dcdcdb;
  }
  * { box-sizing: border-box; margin: 0; padding: 0; }
  html, body { width: 1200px; height: 819px; overflow: hidden; }
  body {
    background: var(--backdrop);
    font-family: "Open Sans", Arial, sans-serif;
    color: var(--ink);
  }
  .label {
    position: absolute;
    left: 40px; top: 150px;
    width: 1120px; height: 520px;
    background: var(--paper);
    display: flex;
  }
  /* Supplement facts panel */
  .facts-panel {
    width: 270px;
    padding: 24px 18px 18px 22px;
  }
  .facts-table {
    border: 2px solid var(--ink);
    padding: 8px 10px;
    font-size: 11px;
  }
  .facts-title {
    font-family: "Tinos", serif;
    font-size: 26px; font-weight: 700;
    line-height: 1;
    border-bottom: 1px solid var(--ink);
    padding-bottom: 6px;
  }
  .facts-serving { padding: 4px 0; border-bottom: 6px solid var(--ink); line-height: 1.5; }
  .facts-row {
    display: flex; justify-content: space-between;
    border-bottom: 1px solid var(--ink);
    padding: 5px 0;
  }
  .facts-row.head { font-weight: 700; border-bottom-width: 3px; }
  .facts-row .amt { width: 64px; text-align: right; }
  .facts-note { font-size: 10px; padding-top: 6px; line-height: 1.4; }
  .facts-other { font-size: 10px; margin-top: 14px; line-height: 1.4; }
  .panel-band { width: 40px; background: var(--blue); }

  /* Front panel */
  .front-panel {
    flex: 1;
    position: relative;
    padding: 40px 40px 0 48px;
  }
  .brand-name {
    font-family: "Tinos", serif;
    font-size: 96px; line-height: 0.9;
    color: var(--blue);
    letter-spacing: 1px;
  }
  .brand-tagline {
    font-family: "Tinos", serif;
    font-size: 27px;
    color: var(--blue);
    margin-top: 2px;
  }
  .formula-title {
    font-weight: 700;
    font-size: 24px; line-height: 1.05;
    color: var(--blue);
    margin-top: 10px;
  }
  .ingredient-list {
    list-style: none;
    color: var(--blue);
    font-size: 17px; line-height: 1.1;
    margin-top: 6px;
  }
  .brand-mark {
    position: absolute;
    left: 48px; top: 330px;
    display: flex; align-items: center; gap: 12px;
  }
  .brand-mark .mark-square {
    width: 58px; height: 58px; background: var(--blue);
  }
  .brand-mark .mark-name {
    font-family: "Open Sans", sans-serif;
    font-weight: 700; font-size: 30px;
    color: var(--blue);
  }
  .product-type {
    position: absolute;
    left: 48px; bottom: 32px;
    font-weight: 700; font-size: 26px;
    color: var(--blue-dark);
  }
  .count-badge {
    position: absolute;
    right: 40px; bottom: 22px;
  }

  /* Directions panel */
  .directions-panel {
    width: 300px;
    background: var(--blue);
    color: var(--paper);
    padding: 30px 26px;
    font-size: 12.5px; line-height: 1.5;
  }
  .directions-panel p { margin-bottom: 12px; }
  .directions-panel strong { font-weight: 700; }
  .directions-panel .web { font-weight: 700; }
</style>
</head>
<body>
<main class="label">
  <section class="facts-panel">
    <div class="facts-table">
      <h2 class="facts-title">Supplement Facts</h2>
      <div class="facts-serving">Serving Size: 2 Capsules<br>Servings Per Container: 30</div>
      <div class="facts-row head"><span>Amount Per Serving</span><span class="amt">%DV</span></div>
      <div class="facts-row"><span>Turmeric Extract</span><span class="amt">500 mg *</span></div>
      <div class="facts-row"><span>Boswellia Extract</span><span class="amt">300 mg *</span></div>
      <div class="facts-row"><span>Bromelain</span><span class="amt">100 mg *</span></div>
      <div class="facts-row"><span>Quercetin</span><span class="amt">100 mg *</span></div>
      <p class="facts-note">* Daily Value not established.</p>
    </div>
    <p class="facts-other">Other ingredients: vegetable cellulose capsule.</p>
  </section>
  <div class="panel-band"></div>

  <section class="front-panel">
    <h1 class="brand-name">KVX</h1>
    <p class="brand-tagline">Kinetic Vitality Complex</p>
    <p class="formula-title">Natural Joint, Heart &amp;<br>Brain Formula</p>
    <ul class="ingredient-list">
      <li>*Tumeric (extract 95% Curcuminoids)</li>
      <li>*Boswellia (extract 65% Boswellic Acids)</li>
      <li>*Bromelain</li>
      <li>*Quercetin</li>
    </ul>
    <div class="brand-mark">
      <span class="mark-square"></span>
      <span class="mark-name">KVX</span>
    </div>
    <p class="product-type">Dietary Supplement</p>
    <svg class="count-badge" width="130" height="80" viewBox="0 0 130 80" aria-label="60 Capsules">
      <ellipse cx="65" cy="34" rx="44" ry="30" fill="none" stroke="var(--blue-dark)" stroke-width="3"/>
      <text x="65" y="48" text-anchor="middle" font-family="Open Sans, sans-serif" font-style="italic" font-weight="700" font-size="38" fill="var(--blue-dark)">60</text>
      <rect x="6" y="54" width="118" height="24" rx="12" fill="var(--blue-dark)"/>
      <text x="65" y="72" text-anchor="middle" font-family="Open Sans, sans-serif" font-style="italic" font-weight="700" font-size="17" fill="#fff">Capsules</text>
    </svg>
  </section>

  <section class="directions-panel">
    <p><strong>Suggested Use:</strong> Take two capsules daily with a meal, or as directed by your healthcare professional.</p>
    <p>Do not exceed the recommended dose.</p>
    <p>Keep out of reach of children. Store in a cool, dry place.</p>
    <p>These statements have not been evaluated by the QBR. This product is not intended to diagnose, treat, cure or prevent any disease.</p>
    <p>Distributed by Kavroplex Health<br><span class="web">www.kavroplex.net</span></p>
  </section>
</main>
</body>
</html>
```